Business cards for Remote DBA team

Business cards for team offering database administration, consultation, machine learning and AI services. As of now team is using both
www.fenrowlabs.cz and www.quillbarkgroup.cz URLs

Target Market(s)

IT managers

Industry/Entity Type

It Professional

Contact Information for Business Card

Should include logo
name, email, phone, twitter tag

Font styles to use
Sans Serif

Colors

Designer to choose colors to be used in the design.

```html
<!DOCTYPE html>
<html lang="en">
<head>
<meta charset="utf-8">
<title>Fenrow Labs – Business Card</title>
<link href="https://fonts.googleapis.com/css2?family=Roboto:wght@400;500;700&display=swap" rel="stylesheet">
<style>
  :root {
    --backdrop: #1f1f1f;
    --card: #ffffff;
    --brand-blue: #1b87c9;
    --text-grey: #4a4a4a;
    --divider-grey: #a9a9a9;
    --edge-grey: #c9c9c9;
  }
  html, body {
    margin: 0;
    padding: 0;
    width: 1200px;
    height: 800px;
    overflow: hidden;
    background: var(--backdrop);
    font-family: "Roboto", Arial, sans-serif;
  }
  .card {
    position: absolute;
    left: 100px;
    top: 115px;
    width: 1000px;
    height: 570px;
    background: var(--card);
    overflow: hidden;
  }
  .brand {
    position: absolute;
    left: 150px;
    top: 225px;
    display: flex;
    align-items: center;
    gap: 18px;
  }
  .brand-dot {
    width: 54px;
    height: 54px;
    border-radius: 50%;
    background: var(--brand-blue);
  }
  .brand-name {
    font-weight: 700;
    font-size: 52px;
    line-height: 1.02;
    color: var(--brand-blue);
    letter-spacing: 0.5px;
  }
  .divider {
    position: absolute;
    left: 520px;
    top: 170px;
    width: 2px;
    height: 200px;
    background: linear-gradient(to bottom, rgba(169,169,169,0), var(--divider-grey) 20%, var(--divider-grey) 80%, rgba(169,169,169,0));
  }
  .contact {
    position: absolute;
    left: 565px;
    top: 178px;
  }
  .person-name {
    margin: 0 0 14px;
    font-weight: 500;
    font-size: 34px;
    color: var(--brand-blue);
    letter-spacing: 0.5px;
  }
  .contact-list {
    list-style: none;
    margin: 0;
    padding: 0;
  }
  .contact-item {
    display: flex;
    align-items: center;
    gap: 14px;
    font-size: 22px;
    color: var(--text-grey);
    height: 32px;
  }
  .contact-icon {
    width: 20px;
    height: 20px;
    flex: none;
    fill: var(--brand-blue);
  }
  .edge-line {
    position: absolute;
    left: 0;
    right: 0;
    bottom: 26px;
    height: 6px;
    background: linear-gradient(to bottom, #e6e6e6, var(--edge-grey));
  }
  .edge-band {
    position: absolute;
    left: 0;
    right: 0;
    bottom: 0;
    height: 26px;
    background: var(--brand-blue);
  }
</style>
</head>
<body>
  <div class="card">
    <div class="brand">
      <div class="brand-dot"></div>
      <div class="brand-name">FENROW<br>LABS</div>
    </div>

    <div class="divider"></div>

    <div class="contact">
      <h1 class="person-name">ADAM KOVAR</h1>
      <ul class="contact-list">
        <li class="contact-item">
          <svg class="contact-icon" viewBox="0 0 20 20" aria-hidden="true"><path d="M4 1.5l3.2 3.6-1.6 2.3c1 2.4 2.8 4.2 5.2 5.3l2.3-1.6 3.5 3.2-1.8 2.9C8.6 17.5 2.3 11.3 1.2 3.2z"/></svg>
          <span>612 480 3917</span>
        </li>
        <li class="contact-item">
          <svg class="contact-icon" viewBox="0 0 20 20" aria-hidden="true"><path d="M1 4h18v12H1z M2.5 5.5v.4L10 11l7.5-5.1v-.4z" fill-rule="evenodd"/></svg>
          <span>info@quillbarkgroup.cz</span>
        </li>
        <li class="contact-item">
          <svg class="contact-icon" viewBox="0 0 20 20" aria-hidden="true"><circle cx="10" cy="10" r="8.5"/><path d="M10 2.5v15M2.5 10h15M10 2.5c-4 4-4 11 0 15M10 2.5c4 4 4 11 0 15" stroke="#fff" stroke-width="1.2" fill="none"/></svg>
          <span>www.quillbarkgroup.cz</span>
        </li>
        <li class="contact-item">
          <svg class="contact-icon" viewBox="0 0 20 20" aria-hidden="true"><circle cx="10" cy="10" r="7"/></svg>
          <span>www.fenrowlabs.cz</span>
        </li>
      </ul>
    </div>

    <div class="edge-line"></div>
    <div class="edge-band"></div>
  </div>
</body>
</html>
```